New professional looking flyer for company

I need our flyer updated my flyer is the Lvb flyer Have attached current flyer so you know what services need to be listed. Want it to be in mainly dark colours like black and dark grey with pops of light grey, silver or white. i have added several photos for you to choose which ones work best with your design would like The photos to be in colour for the flyer. But can have a mix of greyscale if that works for your design j have attached another companies flyers as design ideas to show what I am looking for

Target Market(s)

new clients

Industry/Entity Type

transport and earthmoving

Colors

Designer to choose colors to be used in the design.

Requirements
Nice to have
• Look professional
Should not have
• No orange or red or green

```html
<!DOCTYPE html>
<html lang="en">
<head>
<meta charset="utf-8">
<title>Lvb Pty Ltd – Our Services</title>
<link rel="stylesheet" href="https://fonts.googleapis.com/css2?family=Exo+2:wght@500;600;700;800&display=swap">
<style>
  :root {
    --page-bg: #1f1f1f;
    --ink-black: #151515;
    --panel-dark: #231f1e;
    --paper: #ebebeb;
    --text-dark: #2a2a2a;
    --silver: #cfd2d4;
    --gold: #b8862e;
    --white: #ffffff;
    --sky-black: #0e0e0e;
    --truck-grey: #3b3936;
    --dirt-deep: #8a5434;
    --dirt-light: #b8784e;
  }
  * { margin: 0; padding: 0; box-sizing: border-box; }
  html, body {
    width: 669px; height: 1200px; overflow: hidden;
    background: var(--page-bg);
    font-family: "Exo 2", Arial, sans-serif;
  }
  .flyer {
    position: absolute; left: 0; top: 167px;
    width: 669px; height: 865px; overflow: hidden;
    background: var(--paper);
  }
  .masthead {
    position: absolute; left: 0; top: 0; width: 669px; height: 130px;
    background: radial-gradient(ellipse at 50% 40%, #3a3a3a 0%, #181818 55%, #0c0c0c 100%);
  }
  .brand-name {
    position: absolute; left: 0; top: 30px; width: 669px; text-align: center;
    font-weight: 800; font-size: 54px; letter-spacing: 2px; color: var(--silver);
    z-index: 2;
  }
  .hero-photo {
    position: absolute; left: 0; top: 92px; width: 669px; height: 272px;
    background:
      radial-gradient(ellipse 55% 40% at 72% 78%, rgba(30,32,38,0.85) 0%, rgba(30,32,38,0) 100%),
      radial-gradient(ellipse 35% 30% at 18% 42%, rgba(35,35,35,0.8) 0%, rgba(35,35,35,0) 100%),
      linear-gradient(180deg, var(--sky-black) 0%, #1c1c1c 14%, var(--truck-grey) 34%, var(--dirt-deep) 52%, var(--dirt-light) 70%, #a46f4d 86%, #6e5444 100%);
    clip-path: polygon(0 0, 100% 0, 100% 92%, 88% 95%, 70% 93%, 55% 100%, 0 100%);
  }
  .section-band {
    position: absolute; left: 0; top: 304px; width: 282px; height: 60px;
    background: var(--panel-dark);
    clip-path: polygon(0 0, 100% 0, 100% 88%, 94% 100%, 0 100%);
  }
  .section-title {
    position: absolute; left: 24px; top: 307px;
    font-weight: 800; font-size: 38px; color: var(--silver);
  }
  .services {
    position: absolute; list-style: none;
    font-weight: 600; font-size: 20px; color: var(--text-dark); line-height: 1.2;
  }
  .services li { position: relative; padding-left: 26px; height: 39.7px; }
  .services li::before {
    content: ""; position: absolute; left: 0; top: 4px; width: 15px; height: 15px;
    border: 2px solid var(--gold); border-radius: 50%;
  }
  .services li::after {
    content: ""; position: absolute; left: 4px; top: 7px; width: 5px; height: 8px;
    border: solid var(--gold); border-width: 0 2px 2px 0; transform: rotate(40deg);
  }
  .services-left { left: 24px; top: 389px; }
  .services-right { left: 398px; top: 389px; }
  .divider {
    position: absolute; left: 24px; top: 658px; width: 381px; height: 2px;
    background: linear-gradient(90deg, var(--gold) 0 50%, var(--ink-black) 50% 100%);
  }
  .offer-intro {
    position: absolute; left: 23px; top: 690px;
    font-weight: 500; font-size: 16.5px; color: var(--text-dark);
  }
  .offer-call {
    position: absolute; left: 23px; top: 712px;
    font-weight: 800; font-size: 23px; line-height: 28px; color: var(--gold);
  }
  .side-photo {
    position: absolute; left: 398px; top: 640px; width: 271px; height: 150px;
    background:
      radial-gradient(ellipse 60% 45% at 60% 35%, rgba(200,190,170,0.55) 0%, rgba(200,190,170,0) 100%),
      linear-gradient(180deg, #4a4640 0%, #5e574c 40%, #2b2a28 80%, #151515 100%);
  }
  .footer-edge {
    position: absolute; left: 0; top: 760px; width: 669px; height: 30px;
  }
  .footer {
    position: absolute; left: 0; top: 785px; width: 669px; height: 80px;
    background: var(--ink-black);
  }
  .phone {
    position: absolute; left: 23px; top: 804px; display: flex; align-items: center; gap: 16px;
    font-weight: 800; font-size: 41px; color: var(--white); letter-spacing: 1px;
  }
  .contact {
    position: absolute; left: 384px; top: 815px; list-style: none;
    font-weight: 600; font-size: 11px; color: var(--white); line-height: 19px;
  }
  .contact li { display: flex; align-items: center; gap: 7px; }
</style>
</head>
<body>
  <main class="flyer">
    <header class="masthead"></header>
    <div class="hero-photo" role="img" aria-label="Photo of road train trucks with tipper trailers and a water tanker on red outback dirt"></div>
    <div class="brand-name">Lvb Pty Ltd</div>
    <div class="section-band"></div>
    <h1 class="section-title">Our Services</h1>

    <ul class="services services-left">
      <li>Over size loads / Hot Shot Loads</li>
      <li>Heavy Vehicle Recovery Services</li>
      <li>Potable Water Deliveries</li>
      <li>Road Building / Maintenance</li>
      <li>Earthworks</li>
      <li>Sand &amp; Metal Supply &amp; Cartage</li>
    </ul>
    <ul class="services services-right">
      <li>Road Train Tippers</li>
      <li>Road Train Tankers</li>
      <li>Road Train Flat Tops</li>
      <li>Drop Deck Trailers</li>
      <li>Mine Site accredited<br>equipment &amp; Operators</li>
    </ul>

    <div class="divider"></div>
    <p class="offer-intro">We offer a large range of services not listed so</p>
    <p class="offer-call">Call us today for a personalised<br>quote to suit your needs.</p>

    <div class="side-photo" role="img" aria-label="Photo of an oversize road train truck hauling a site building"></div>

    <svg class="footer-edge" viewBox="0 0 669 30" preserveAspectRatio="none" aria-hidden="true">
      <polygon points="0,18 358,18 398,0 669,0 669,30 0,30" fill="#151515"/>
    </svg>
    <footer class="footer"></footer>

    <div class="phone">
      <svg width="32" height="32" viewBox="0 0 32 32" aria-hidden="true">
        <circle cx="16" cy="16" r="16" fill="#b8862e"/>
        <path d="M11 8c1-1 2-1 3 0l2 3c.5 1 0 2-1 2.5l-1 .7c.8 2 2.5 3.8 4.5 4.6l.7-1c.6-1 1.6-1.4 2.5-.9l3 2c1 .6 1 1.8 0 2.8-1.5 1.5-3.5 2-5.5 1C14 21 11 18 9.5 14c-.8-2.2 0-4.3 1.5-6z" fill="#151515"/>
      </svg>
      <span>043 555 0192</span>
    </div>

    <ul class="contact">
      <li>
        <svg width="8" height="11" viewBox="0 0 8 11" aria-hidden="true"><path d="M4 0a4 4 0 0 1 4 4c0 3-4 7-4 7S0 7 0 4a4 4 0 0 1 4-4z" fill="#b8862e"/><circle cx="4" cy="4" r="1.5" fill="#151515"/></svg>
        Depot: Lot 14, Ridgeline Road Dry Creek
      </li>
      <li>
        <svg width="9" height="7" viewBox="0 0 9 7" aria-hidden="true"><rect width="9" height="7" fill="#b8862e"/><path d="M0 0l4.5 3.5L9 0" stroke="#151515" fill="none"/></svg>
        info@lvbservices.com.au
      </li>
    </ul>
  </main>
</body>
</html>
```